Innovative Consulting Firm Needs New Business Cards and Stationary

Our Innovative Consulting Firm, Larkfield Consulting, is in need of new business cards and stationary designs. We want two-sided cards that incorporate our logo, which is attached. We are looking for something not too formal, but is professional and slick.

Card should have the following information:
Name (ex. Tom Bradley)
Title (ex. Manager)
Address (ex. 24680 Cedar Lane)
Address 2 (ex. Suite 100)
City
State
Zip Code
Mobile
Email

The card should also have our website: www.larkfieldconsulting.example

Industry/Entity Type

Management Consulting

Contact Information for Business Card

Name (ex. Tom Bradley)
Title (ex. Manager)
Address 2 (ex. Suite 100)
City
State
Zip Code
Mobile
Email

Font styles to use
Sans Serif

Requirements
Must have
• The colors on the card must match the colors in the logo. The exact color codes are attached in a pdf.
Nice to have
• The Company's Tagline is "Focused on your Future". This might be nice to incorporate, but not necessary.

```html
<!DOCTYPE html>
<html lang="en">
<head>
<meta charset="utf-8">
<title>Larkfield Consulting – Business Cards</title>
<link rel="stylesheet" href="https://fonts.googleapis.com/css2?family=Arimo:wght@400;700&family=Gochi+Hand&display=swap">
<style>
  :root {
    --backdrop: #1c1c1c;
    --brand-blue: #1f4e79;
    --brand-yellow: #f2b62c;
    --brand-yellow-deep: #e0a11d;
    --paper: #f4f4f4;
    --paper-shade: #e2e2e2;
    --white: #ffffff;
  }
  * { box-sizing: border-box; margin: 0; padding: 0; }
  html, body {
    width: 1200px; height: 800px; overflow: hidden;
    background: var(--backdrop);
    font-family: "Arimo", Arial, sans-serif;
  }
  .canvas {
    width: 1200px; height: 800px;
    display: flex; align-items: center; justify-content: center; gap: 50px;
  }
  .card {
    width: 525px; height: 300px; position: relative; overflow: hidden;
    border-radius: 2px;
  }

  /* Front side */
  .card--front { display: flex; }
  .front__brand-panel {
    width: 55%; height: 100%; position: relative;
    background: linear-gradient(135deg, var(--white), var(--paper) 55%, var(--paper-shade));
  }
  .brand-lockup {
    position: absolute; top: 36px; left: 28px;
    display: flex; align-items: center; gap: 8px;
  }
  .brand-lockup__dot {
    width: 12px; height: 12px; border-radius: 50%; background: var(--brand-yellow);
  }
  .brand-lockup__name {
    color: var(--brand-blue); font-weight: 700; font-size: 21px; letter-spacing: 0.2px;
  }
  .tagline {
    position: absolute; left: 24px; bottom: 34px;
    background: var(--brand-blue); color: var(--white);
    border-radius: 12px; padding: 5px 18px;
    font-family: "Gochi Hand", cursive; font-size: 19px; letter-spacing: 0.5px;
  }
  .front__contact-panel {
    width: 45%; height: 100%;
    background: linear-gradient(160deg, var(--brand-yellow), var(--brand-yellow-deep));
    padding: 34px 12px 0 18px; color: var(--white);
  }
  .contact-row {
    display: flex; align-items: flex-start; gap: 9px; margin-bottom: 11px;
    font-size: 12px; line-height: 1.3;
  }
  .contact-row p { min-width: 0; overflow-wrap: anywhere; }
  .contact-row svg { flex: none; width: 13px; height: 13px; margin-top: 1px; }
  .contact-row--person { margin-bottom: 18px; }
  .person__name { color: var(--brand-blue); font-weight: 700; font-size: 16px; line-height: 1.1; }
  .person__title { color: var(--brand-blue); font-weight: 700; font-size: 11px; }

  /* Back side */
  .card--back {
    background: var(--brand-blue);
    display: flex; align-items: center; justify-content: center;
  }
  .back__lockup { display: flex; align-items: center; gap: 12px; }
  .back__dot { width: 18px; height: 18px; border-radius: 50%; background: var(--brand-yellow); }
  .back__name { color: var(--white); font-weight: 700; font-size: 36px; }
</style>
</head>
<body>
<main class="canvas">
  <section class="card card--front" aria-label="Business card front">
    <div class="front__brand-panel">
      <div class="brand-lockup">
        <span class="brand-lockup__dot"></span>
        <span class="brand-lockup__name">Larkfield Consulting</span>
      </div>
      <p class="tagline">Focused on your Future</p>
    </div>
    <div class="front__contact-panel">
      <div class="contact-row contact-row--person">
        <svg viewBox="0 0 16 16" aria-hidden="true"><circle cx="8" cy="4.5" r="3.5" fill="var(--brand-blue)"/><path d="M1 16c0-5 3-7 7-7s7 2 7 7z" fill="var(--brand-blue)"/></svg>
        <div>
          <p class="person__name">Tom Bradley</p>
          <p class="person__title">Manager</p>
        </div>
      </div>
      <div class="contact-row">
        <svg viewBox="0 0 16 16" aria-hidden="true"><path d="M8 0a5.5 5.5 0 0 0-5.5 5.5C2.5 10 8 16 8 16s5.5-6 5.5-10.5A5.5 5.5 0 0 0 8 0zm0 8a2.5 2.5 0 1 1 0-5 2.5 2.5 0 0 1 0 5z" fill="var(--brand-blue)"/></svg>
        <p>24680 Cedar Lane<br>Suite 100, City, State<br>Zip Code</p>
      </div>
      <div class="contact-row">
        <svg viewBox="0 0 16 16" aria-hidden="true"><path d="M3.5 1 6 4 4.5 6c1 2.2 3.3 4.5 5.5 5.5L12 10l3 2.5-1.5 2.5C7.5 15 1 8.5 1 2.5z" fill="none" stroke="var(--brand-blue)" stroke-width="1.4"/></svg>
        <p>0123456789</p>
      </div>
      <div class="contact-row">
        <svg viewBox="0 0 16 16" aria-hidden="true"><rect x="1" y="3" width="14" height="10" fill="none" stroke="var(--brand-blue)" stroke-width="1.4"/><path d="M1 3l7 6 7-6" fill="none" stroke="var(--brand-blue)" stroke-width="1.4"/></svg>
        <p>tom@larkfieldmail.example</p>
      </div>
      <div class="contact-row">
        <svg viewBox="0 0 16 16" aria-hidden="true"><circle cx="8" cy="8" r="7" fill="none" stroke="var(--brand-blue)" stroke-width="1.4"/><path d="M1 8h14M8 1c-3 4-3 10 0 14M8 1c3 4 3 10 0 14" fill="none" stroke="var(--brand-blue)" stroke-width="1.2"/></svg>
        <p>www.larkfieldconsulting.example</p>
      </div>
    </div>
  </section>

  <section class="card card--back" aria-label="Business card back">
    <div class="back__lockup">
      <span class="back__dot"></span>
      <span class="back__name">Larkfield Consulting</span>
    </div>
  </section>
</main>
</body>
</html>
```